Kelvane Plumbing Business cards

Company is Kelvane Plumbing.
name Dashel Morrowby, I am a plumber, drainer, gasfitter and roofer
Mobile: 0431 906 154
Email address: info@kelvaneplumbing.example (check out my website for some ideas)
Website: www.kelvaneplumbing.example
ABN: 82 916 203 471
LIC: 604517K

I am reliable all round plumber. I am a 24 hour emergency service. Kelvane Plumbing is a professional plumbing service in the Illawarra, South Coast, Southern Sydney and Southern Highland regions of NSW. We offer a 24 hour emergency service for piece of mind to our customers. Call us now to see how we can help you. Kelvane Plumbing approaches every job with attention to detail and excellent customer service. With our superior workmanship you can be confident that the job will be done right the first time around. You can rest assured with results that are guaranteed to last.

Target Market(s)

the general public

Contact Information for Business Card

look up website for some ideas something with similar colours to logo and new modern and to catch the eye.

Colors
fdfdfd
ffffff
000000
7f7f7f
aaaaaa
33a6d7
0492cd

Requirements
Must have
• all contact details
• company- Kelvane Plumbing
• name- Dashel Morrowby
• number mobile- 0431 906 154
• Email address- info@kelvaneplumbing.example
• Website- www.kelvaneplumbing.example
• ABN- 82 916 203 471
• LIC- 604517K

```html
<!DOCTYPE html>
<html lang="en">
<head>
<meta charset="utf-8">
<title>Kelvane Plumbing – Business Cards</title>
<link rel="stylesheet" href="https://fonts.googleapis.com/css2?family=PT+Sans:wght@400;700&family=PT+Sans+Narrow:wght@400&display=swap">
<style>
  :root {
    --page: #e9e7e4;
    --card: #1f1e20;
    --blue: #0492cd;
    --blue-light: #33a6d7;
    --grey: #aaaaaa;
    --white: #fdfdfd;
    --ink: #000000;
  }
  * { box-sizing: border-box; margin: 0; padding: 0; }
  html, body { width: 1200px; height: 900px; overflow: hidden; }
  body {
    background: var(--page);
    font-family: "PT Sans", Arial, sans-serif;
    position: relative;
  }
  .card {
    position: absolute;
    left: 270px;
    width: 660px;
    height: 377px;
    background: var(--card);
    border-radius: 4px;
    box-shadow: 0 6px 18px rgba(0,0,0,.25);
    overflow: hidden;
  }
  .card--back { top: 48px; }
  .card--front { top: 475px; }

  /* back */
  .back-mark {
    position: absolute;
    inset: 0;
    display: flex;
    align-items: center;
    justify-content: center;
    gap: 18px;
  }
  .back-mark__dot {
    width: 46px; height: 46px;
    border-radius: 50%;
    border: 6px solid var(--blue);
  }
  .back-mark__name {
    font-size: 44px;
    font-weight: 700;
    color: var(--blue);
    letter-spacing: 1px;
  }

  /* front */
  .front-art { position: absolute; left: 0; top: 0; }
  .contact-row {
    position: absolute;
    left: 108px;
    height: 44px;
    display: flex;
    align-items: center;
  }
  .contact-row--phone { top: 76px; }
  .contact-row--email { top: 133px; }
  .contact-row--web { top: 190px; }
  .contact-row__icon {
    width: 42px; height: 44px;
    background: var(--blue);
    display: flex; align-items: center; justify-content: center;
  }
  .contact-row__icon svg { width: 26px; height: 26px; }
  .contact-row__text {
    height: 44px;
    width: 280px;
    border: 1.5px solid var(--blue);
    border-left: none;
    border-radius: 0 6px 6px 0;
    color: var(--white);
    font-size: 15px;
    display: flex; align-items: center;
    padding-left: 12px;
    white-space: nowrap;
  }
  .holder {
    position: absolute;
    left: 452px; top: 52px;
    right: 14px;
  }
  .holder__name {
    font-family: "PT Sans Narrow", "Arial Narrow", sans-serif;
    font-size: 27px;
    line-height: 1.1;
    color: var(--blue-light);
  }
  .holder__role {
    font-size: 12px;
    color: var(--grey);
    margin-top: 4px;
    white-space: nowrap;
  }
  .front-brand {
    position: absolute;
    left: 452px; top: 168px;
    font-size: 30px;
    font-weight: 700;
    color: var(--blue);
    line-height: 1.1;
    letter-spacing: 1px;
  }
  .info-band {
    position: absolute;
    left: 0; right: 0; bottom: 0;
    height: 44px;
    background: linear-gradient(90deg, var(--blue-light), var(--blue));
    display: flex; justify-content: space-between; align-items: center;
    padding: 0 30px;
    color: var(--ink);
    font-weight: 700;
    font-size: 16px;
  }
</style>
</head>
<body>

<section class="card card--back" aria-label="Card back">
  <div class="back-mark">
    <span class="back-mark__dot"></span>
    <span class="back-mark__name">Kelvane Plumbing</span>
  </div>
</section>

<section class="card card--front" aria-label="Card front">
  <svg class="front-art" width="660" height="377" viewBox="0 0 660 377" aria-hidden="true">
    <polygon points="0,38 108,76 108,118 0,104" fill="#0492cd"/>
    <polygon points="0,120 108,133 108,177 0,186" fill="#33a6d7"/>
    <polygon points="0,204 108,190 108,234 0,280" fill="#0492cd"/>
  </svg>

  <div class="contact-row contact-row--phone">
    <div class="contact-row__icon">
      <svg viewBox="0 0 24 24"><rect x="7" y="3" width="10" height="18" rx="2" fill="#000"/><rect x="9" y="6" width="6" height="6" fill="#0492cd"/></svg>
    </div>
    <div class="contact-row__text">0431 906 154</div>
  </div>
  <div class="contact-row contact-row--email">
    <div class="contact-row__icon">
      <svg viewBox="0 0 24 24"><rect x="2" y="5" width="20" height="14" fill="none" stroke="#000" stroke-width="2"/><polyline points="2,5 12,13 22,5" fill="none" stroke="#000" stroke-width="2"/></svg>
    </div>
    <div class="contact-row__text">info@kelvaneplumbing.example</div>
  </div>
  <div class="contact-row contact-row--web">
    <div class="contact-row__icon">
      <svg viewBox="0 0 24 24"><circle cx="12" cy="12" r="9" fill="none" stroke="#000" stroke-width="2"/><ellipse cx="12" cy="12" rx="4" ry="9" fill="none" stroke="#000" stroke-width="1.6"/><line x1="3" y1="12" x2="21" y2="12" stroke="#000" stroke-width="1.6"/></svg>
    </div>
    <div class="contact-row__text">www.kelvaneplumbing.example</div>
  </div>

  <div class="holder">
    <div class="holder__name">Dashel Morrowby</div>
    <div class="holder__role">plumber, drainer, gasfitter and roofer</div>
  </div>

  <div class="front-brand">Kelvane<br>Plumbing</div>

  <div class="info-band">
    <span>ABN: 82 916 203 471</span>
    <span>LIC: 604517K</span>
  </div>
</section>

</body>
</html>
```